Business cards for KORU Real Estate Holdings LLC

We need a cool, original business card design for a company based in the Washington DC metropolitan area. We are a new energetic and passionate Real Estate Investing Company that invests in all types of real estate; commercial, residential, industrial etc.

Our company color is Red since it reflects action, energy and speed; it is assertive confident, energizing, exciting, powerful, passionate and determined. So we would like business card communicate those qualities to the audience.

Our audiences are investors that want to invest with us, real estate sellers, buyers, and tenants who lease from us.

Our logo is attached

```html
<!DOCTYPE html>
<html lang="en">
<head>
<meta charset="utf-8">
<title>KORU Real Estate Holdings LLC — Business Card</title>
<link rel="stylesheet" href="https://fonts.googleapis.com/css2?family=Exo+2:wght@400;500;600;700&family=Rajdhani:wght@500;600;700&display=swap">
<style>
  :root {
    --page: #e9e9e9;
    --card: #f7f7f7;
    --card-edge: #dcdcdc;
    --band: #353535;
    --red: #d8262c;
    --ink: #2e2e2e;
    --ink-soft: #5a5a5a;
    --on-band: #ffffff;
    --icon-disc: #d9d9d9;
    --icon-ink: #3a3a3a;
  }
  * { margin: 0; padding: 0; box-sizing: border-box; }
  html, body { width: 1200px; height: 769px; overflow: hidden; }
  body {
    background: var(--page);
    font-family: "Exo 2", "Segoe UI", sans-serif;
    color: var(--ink);
    position: relative;
  }
  .card {
    position: absolute;
    left: 150px; top: 124px;
    width: 900px; height: 522px;
    background: var(--card);
    border: 1px solid var(--card-edge);
    border-radius: 6px;
    overflow: hidden;
    box-shadow: 0 10px 30px rgba(0,0,0,.12);
  }
  .brand {
    position: absolute; left: 0; right: 0; top: 48px;
    display: flex; justify-content: center; align-items: center; gap: 16px;
  }
  .brand-mark { width: 46px; height: 46px; background: var(--red); }
  .brand-name { color: var(--ink); font-weight: 700; line-height: 1; }
  .brand-name .word { display: block; font-size: 52px; letter-spacing: 2px; }
  .brand-name .tag { display: block; font-size: 14px; letter-spacing: 1.5px; margin-top: 4px; }

  .info-band {
    position: absolute; left: 0; right: 0; top: 188px; height: 240px;
    background: var(--band);
    border-top: 5px solid var(--red);
    border-bottom: 5px solid var(--red);
    display: grid; grid-template-columns: 1fr 1fr 1fr;
    padding: 0 30px;
  }
  .info-col {
    display: flex; flex-direction: column; align-items: center;
    padding-top: 40px; color: var(--on-band); text-align: center;
    white-space: nowrap;
  }
  .icon-disc {
    width: 74px; height: 74px; border-radius: 50%;
    background: var(--icon-disc); border: 3px solid #8a8a8a;
    display: flex; align-items: center; justify-content: center;
    margin-bottom: 24px;
  }
  .person-name {
    font-family: "Rajdhani", "Arial Narrow", sans-serif;
    font-weight: 600; font-size: 34px; letter-spacing: 1px; line-height: 1;
  }
  .person-role { font-size: 12px; letter-spacing: 1.5px; margin-top: 6px; }
  .contact-line { font-size: 21px; letter-spacing: .3px; line-height: 1.35; }
  .phone-line { font-size: 23px; letter-spacing: 2px; line-height: 1.3; }

  .social-strip {
    position: absolute; left: 0; right: 0; top: 432px; height: 78px;
    display: flex; align-items: center; padding-left: 80px; gap: 46px;
  }
  .follow-title { font-size: 21px; font-weight: 500; letter-spacing: 1px; line-height: 1; color: var(--ink); }
  .follow-sub { font-size: 9px; letter-spacing: 1px; color: var(--ink-soft); margin-top: 5px; }
  .social-links { display: flex; gap: 22px; }
  .social-slot { width: 22px; height: 22px; background: var(--ink); border-radius: 3px; }
  .card-foot { position: absolute; left: 0; right: 0; bottom: 0; height: 8px; background: var(--red); }
</style>
</head>
<body>
  <article class="card">
    <header class="brand">
      <div class="brand-mark"></div>
      <div class="brand-name">
        <span class="word">KORU</span>
        <span class="tag">REAL ESTATE HOLDINGS LLC</span>
      </div>
    </header>

    <section class="info-band">
      <div class="info-col">
        <div class="icon-disc">
          <svg width="38" height="38" viewBox="0 0 38 38" aria-hidden="true">
            <circle cx="19" cy="13" r="7.5" fill="var(--icon-ink)"/>
            <path d="M5 35c0-9 6-14 14-14s14 5 14 14z" fill="var(--icon-ink)"/>
          </svg>
        </div>
        <div class="person-name">DANA WHITFIELD</div>
        <div class="person-role">GENERAL MANAGER</div>
      </div>
      <div class="info-col">
        <div class="icon-disc">
          <svg width="40" height="40" viewBox="0 0 40 40" aria-hidden="true" fill="none" stroke="var(--icon-ink)" stroke-width="2.4">
            <circle cx="20" cy="20" r="16"/>
            <ellipse cx="20" cy="20" rx="7" ry="16"/>
            <line x1="4" y1="20" x2="36" y2="20"/>
            <path d="M7 11h26M7 29h26"/>
          </svg>
        </div>
        <div class="contact-line">dana@koruholdings.com</div>
        <div class="contact-line">www.koruholdings.com</div>
      </div>
      <div class="info-col">
        <div class="icon-disc">
          <svg width="30" height="40" viewBox="0 0 30 40" aria-hidden="true">
            <rect x="5" y="2" width="20" height="36" rx="3" fill="none" stroke="var(--icon-ink)" stroke-width="2.6"/>
            <rect x="8" y="7" width="14" height="23" fill="var(--icon-ink)"/>
            <circle cx="15" cy="34" r="1.8" fill="var(--icon-ink)"/>
          </svg>
        </div>
        <div class="phone-line">202 418 7395</div>
        <div class="phone-line">202 418 7396</div>
      </div>
    </section>

    <footer class="social-strip">
      <div class="follow">
        <div class="follow-title">FOLLOW US</div>
        <div class="follow-sub">ON SOCIAL NETWORKS</div>
      </div>
      <div class="social-links">
        <span class="social-slot"></span>
        <span class="social-slot"></span>
        <span class="social-slot"></span>
        <span class="social-slot"></span>
      </div>
    </footer>
    <div class="card-foot"></div>
  </article>
</body>
</html>
```